Natural Skincare Product Labels Design

We are looking for a designer to create elegant but quirky, functional product labels for our natural skincare range.
The labels must reflect our brand’s values of simplicity, luxury, and the natural, handmade essence of our products.
https://www.pictogrove.com/marvellaskincare
1. Key Details
Packaging Dimensions
Container Types: Transparent jars.
Sizes for Body Products:
Diameter: 64mm–68mm.
Heights: 80mm, 88mm, and 97mm (lid height: 15mm).
Sizes for Face Creams:
Diameter: 60mm.
Height: 50mm (lid height: 15mm).
Label Fit: For body products, ideally one label size to fit all jar sizes.
For the smaller face cream jars, a separate, tailored label is required.
2. Label Placement
Options include a wrapped-around label or a combination of wrapped-around and top-of-jar elements.
Transparent jars mean the label must leave space for the product to be visible (e.g., partial wrap or cutout areas).
3. Content Requirements
Product Name: Prominently displayed.
Ingredient List: Dedicated space required.
Disclaimer/Usage Instructions: Include space for this information.
4. Design Goals
Look & Feel: Simple, upmarket, and natural, with a handmade essence.
Logo Usage: Our logo is finalized and available in gold, black, and white variants. Use Josefin Bold font for the logo if adjustments are required.
Color Palette: Neutral tones (e.g., whites, blacks, golds) are preferred, with flexibility for subtle pops of color tied to each product’s main ingredient.
5. Imagery
Open to including images and colours (e.g., botanical illustrations) that highlight the main ingredient (e.g., coffee beans, turmeric root, or honeycomb). Also open to labels having a prominent colour to tie it in to the main ingredient.
Alternatively, no images can also work for a clean design.
6. Current Design Context
Our temporary design features gold leaf on top and a simple handmade side label. We’re seeking to elevate this to a more polished, cohesive design.
7. Product Line
- Body Products (Larger Jars)
Tolo Body Butter
Key Ingredients: Guarana & Cupuaçu butter (inspired by Brazil).
Note: “Tolo” is slang for “bum.”
Manuka Honey Body Butter
Key Ingredients: Manuka honey (from New Zealand) & Cupuaçu butter.
Coffee Body Scrub
Key Ingredients: Coffee and Demerara sugar.
Whipped Body Soap - Turmeric
Key Ingredients: Turmeric and Bentonite clay.
Whipped Body Soap - Banana
- Face Products (Smaller Jars)
Face Cream
Key Ingredients: Carrot Oil and Raspberry Oil.
Features natural UV protection.
Good Night Cream
Key Ingredients: Enriched with Magnesium.
Promotes relaxation and restful sleep.
8. Submission Guidelines
Flexibility: Design should allow for consistent branding across all products while accommodating the varying jar sizes and ingredient focus.
Material Considerations: Labels should complement the transparent jars and allow the product inside to remain partially visible.
Print Elements: Incorporating gold accents is a plus but should not overpower the design.
We’re excited to see your vision for a label that celebrates the natural beauty and high quality of our skincare range. Please include mockups to showcase the design in use, particularly on transparent jars of varying sizes.
women 20-50 years of age

```html
<!DOCTYPE html>
<html lang="en">
<head>
<meta charset="utf-8">
<title>Marvella – Manuka Honey Body Butter Label</title>
<link href="https://fonts.googleapis.com/css2?family=Josefin+Sans:wght@400;600&family=Fondamento&display=swap" rel="stylesheet">
<style>
  :root {
    --backdrop: #2e2e2e;
    --label-ink: #2b2925;
    --lid-ink: #323232;
    --gold: #d99a1e;
    --gold-soft: #c48a24;
    --gold-line: #a9802f;
  }
  * { margin: 0; padding: 0; box-sizing: border-box; }
  html, body {
    width: 1200px;
    height: 808px;
    overflow: hidden;
    background: var(--backdrop);
  }
  .canvas {
    position: relative;
    width: 1200px;
    height: 808px;
    font-family: "Josefin Sans", sans-serif;
    color: var(--gold);
  }

  /* Front wrap label */
  .front-label {
    position: absolute;
    left: 110px;
    top: 104px;
    width: 560px;
    height: 600px;
  }
  .front-label__shape { position: absolute; inset: 0; }
  .front-label__brand {
    position: absolute;
    top: 62px;
    width: 100%;
    text-align: center;
    font-size: 15px;
    font-weight: 600;
    letter-spacing: 3px;
    color: var(--gold-soft);
  }
  .front-label__rule {
    position: absolute;
    left: 140px;
    width: 280px;
    height: 1px;
    background: var(--gold-line);
  }
  .front-label__rule--top { top: 200px; }
  .front-label__rule--bottom { top: 458px; }
  .front-label__title {
    position: absolute;
    top: 268px;
    width: 100%;
    text-align: center;
    font-size: 50px;
    font-weight: 400;
    letter-spacing: 1px;
  }
  .front-label__subtitle {
    position: absolute;
    top: 332px;
    width: 100%;
    text-align: center;
    font-size: 34px;
    font-weight: 600;
  }
  .front-label__ingredients {
    position: absolute;
    top: 496px;
    left: 80px;
    right: 80px;
    text-align: center;
    font-family: "Fondamento", cursive;
    font-size: 19px;
    line-height: 1.2;
    color: var(--gold-soft);
  }

  /* Lid top label */
  .lid-label {
    position: absolute;
    left: 720px;
    top: 154px;
    width: 420px;
    height: 420px;
  }
  .lid-label__shape { position: absolute; inset: 0; }
  .lid-label__brand {
    position: absolute;
    top: 176px;
    width: 100%;
    text-align: center;
    font-size: 40px;
    font-weight: 600;
    letter-spacing: 6px;
    color: var(--gold-soft);
  }
  .lid-label__tagline {
    position: absolute;
    top: 230px;
    width: 100%;
    text-align: center;
    font-size: 17px;
    font-weight: 600;
    letter-spacing: 4px;
    color: var(--gold-soft);
  }
</style>
</head>
<body>
<main class="canvas">

  <section class="front-label">
    <svg class="front-label__shape" viewBox="0 0 560 600" width="560" height="600" aria-hidden="true">
      <path d="M0,90 H205 C205,30 240,0 280,0 C320,0 355,30 355,90 H560 V600 H0 Z" fill="var(--label-ink)"/>
      <path d="M34,104 H219 C219,44 250,14 280,14 C310,14 341,44 341,104 H526 A20,20 0 0 0 546,124 V566 A20,20 0 0 0 526,586 H34 A20,20 0 0 0 14,566 V124 A20,20 0 0 0 34,104 Z"
            fill="none" stroke="var(--gold-soft)" stroke-width="2"/>
    </svg>
    <p class="front-label__brand">MARVELLA</p>
    <span class="front-label__rule front-label__rule--top"></span>
    <h1 class="front-label__title">MANUKA HONEY</h1>
    <p class="front-label__subtitle">Body Butter</p>
    <span class="front-label__rule front-label__rule--bottom"></span>
    <p class="front-label__ingredients">Key Ingredients: Manuka honey (from New Zealand) &amp; Cupuaçu butter.</p>
  </section>

  <section class="lid-label">
    <svg class="lid-label__shape" viewBox="0 0 420 420" width="420" height="420" aria-hidden="true">
      <circle cx="210" cy="210" r="208" fill="var(--lid-ink)"/>
      <circle cx="210" cy="210" r="182" fill="none" stroke="var(--gold-soft)" stroke-width="2"/>
    </svg>
    <p class="lid-label__brand">MARVELLA</p>
    <p class="lid-label__tagline">NATURAL SKINCARE</p>
  </section>

</main>
</body>
</html>
```